Re-Design the flow of the Keystride Principles

The keystride principle is a 10 step model that helps teams/organizations become high performing. Attached the model which i created. I love the design as it is but i used a template i don't owe the rights of so i would like to use this platform to see what you can come up with the redesign this flow while keeping the key elements in place. I like the flow, i like the cleanness and i like it to be compact.

Target Market(s)

Organizational change / Leadership/ Consultancy

Industry/Entity Type

Leadership

Requirements
Must have
• Keep as much as possible the flow and feel of the attached
Nice to have
• -Maybe some twist in how the different parts connect (not a must)
Should not have
• Less or more steps than added in the attached file

```html
<!DOCTYPE html>
<html lang="en">
<head>
<meta charset="utf-8">
<title>The Keystride Principles – Design Options</title>
<link href="https://fonts.googleapis.com/css2?family=Montserrat:wght@500;700;800&family=Oswald:wght@300;400;500;600&family=Roboto:wght@700;900&display=swap" rel="stylesheet">
<style>
  :root{
    --page:#5a5a5a;
    --panel:#e2e3e5;
    --blue:#3a97e6;
    --ink:#3c3c3e;
    --ink-soft:#4a4a4a;
    --white:#ffffff;
    --c01:#93c923; --c02:#16b5c1; --c03:#0e9ad6; --c04:#0a5ba6; --c05:#4b5fb0;
    --c06:#5d3b98; --c07:#a52f9b; --c08:#f0245e; --c09:#f45a22; --c10:#fcb514;
  }
  html,body{margin:0;padding:0;overflow:hidden;background:var(--page);}
  .canvas{position:relative;width:1054px;height:1200px;background:var(--page);overflow:hidden;}
  .sheet-label{position:absolute;margin:0;font-family:"Oswald",sans-serif;font-weight:600;font-size:27px;color:var(--white);letter-spacing:-0.3px;}
  .sheet-label--one{left:53px;top:16px;}
  .sheet-label--two{right:65px;top:1150px;}
  .board{position:absolute;left:53px;width:936px;height:527px;display:block;box-shadow:0 2px 6px rgba(0,0,0,.35);}
  .board--one{top:72px;}
  .board--two{top:618px;}
  .defs-holder{position:absolute;width:0;height:0;overflow:hidden;}

  .panel-bg{fill:var(--panel);}
  .map-area{fill:url(#mapTone);}

  /* theme variables */
  .diagram--outline{--ring:var(--blue);--ring-text:var(--white);--arrow:var(--white);--hubring:var(--blue);--label:#3a3a3a;}
  .diagram--solid{--ring:var(--white);--ring-text:#2a2a2a;--arrow:var(--blue);--hubring:#2e2e2e;--label:var(--white);}

  .wedge{fill:var(--white);}
  .diagram--solid .wedge-01{fill:var(--c01);} .diagram--solid .wedge-02{fill:var(--c02);}
  .diagram--solid .wedge-03{fill:var(--c03);} .diagram--solid .wedge-04{fill:var(--c04);}
  .diagram--solid .wedge-05{fill:var(--c05);} .diagram--solid .wedge-06{fill:var(--c06);}
  .diagram--solid .wedge-07{fill:var(--c07);} .diagram--solid .wedge-08{fill:var(--c08);}
  .diagram--solid .wedge-09{fill:var(--c09);} .diagram--solid .wedge-10{fill:var(--c10);}

  .ring{fill:none;stroke:var(--ring);stroke-width:22;}
  .ring-text{font-family:"Montserrat",sans-serif;font-weight:800;font-size:21px;fill:var(--ring-text);letter-spacing:5px;}
  .ring-arrow{fill:none;stroke:var(--arrow);stroke-width:2.6;stroke-linejoin:round;}
  .divider{stroke:var(--panel);stroke-width:9;}
  .hub-ring{fill:var(--hubring);}
  .hub{fill:var(--white);}
  .hub-title{font-family:"Roboto",sans-serif;font-weight:700;font-size:21px;fill:#1f1f1f;text-anchor:middle;}
  .step-no{font-family:"Oswald",sans-serif;font-weight:500;font-size:15px;fill:var(--white);text-anchor:middle;dominant-baseline:central;}
  .step-label{font-family:"Oswald",sans-serif;font-weight:400;font-size:16.5px;fill:var(--label);text-anchor:middle;}
  .restart{font-family:"Oswald",sans-serif;font-weight:400;font-size:15.5px;fill:#444;text-anchor:middle;}

  .marker-disc{stroke:var(--white);stroke-width:4;filter:url(#softShadow);}
  .m01{fill:var(--c01);} .m02{fill:var(--c02);} .m03{fill:var(--c03);} .m04{fill:var(--c04);} .m05{fill:var(--c05);}
  .m06{fill:var(--c06);} .m07{fill:var(--c07);} .m08{fill:var(--c08);} .m09{fill:var(--c09);} .m10{fill:var(--c10);}

  .title{font-family:"Roboto",sans-serif;font-weight:900;font-size:98px;fill:var(--ink);}
  .title-accent{fill:var(--blue);}
  .subtitle{font-family:"Montserrat",sans-serif;font-weight:500;font-size:27px;fill:var(--ink-soft);}

  .goal-box{fill:var(--white);}
  .goal-gem{fill:none;stroke:#8a8a8a;stroke-width:3;stroke-linejoin:round;}
  .goal-title{font-family:"Oswald",sans-serif;font-weight:500;font-size:22px;fill:var(--blue);text-anchor:middle;}
  .goal-list{font-family:"Oswald",sans-serif;font-weight:300;font-size:16px;fill:#444;}
</style>
</head>
<body>
<div class="canvas">

  <svg class="defs-holder" aria-hidden="true">
    <defs>
      <radialGradient id="mapTone" cx="50%" cy="45%" r="60%">
        <stop offset="0" stop-color="#d6d7d9"/>
        <stop offset="1" stop-color="#e2e3e5"/>
      </radialGradient>
      <filter id="softShadow" x="-40%" y="-40%" width="180%" height="180%">
        <feDropShadow dx="0" dy="2" stdDeviation="2.5" flood-color="#000" flood-opacity=".3"/>
      </filter>
      <symbol id="ic-pulse" viewBox="-12 -12 24 24"><g fill="none" stroke="#fff" stroke-width="2" stroke-linejoin="round" stroke-linecap="round"><path d="M0 9 L-8.5 0.5 A4.8 4.8 0 0 1 0 -5.5 A4.8 4.8 0 0 1 8.5 0.5 Z"/><polyline points="-6,0.5 -3,0.5 -1,-3.5 1.5,4 3,0.5 6,0.5"/></g></symbol>
      <symbol id="ic-scope" viewBox="-12 -12 24 24"><g fill="none" stroke="#fff" stroke-width="2" stroke-linejoin="round" stroke-linecap="round"><path d="M-9 -1 L7 -8 L9 -3 L-7 4 Z"/><path d="M0 2 L-5 10 M0 2 L5 10 M0 2 L0 10"/></g></symbol>
      <symbol id="ic-target" viewBox="-12 -12 24 24"><g fill="none" stroke="#fff" stroke-width="2" stroke-linecap="round"><circle r="8"/><circle r="4"/><path d="M0 -11 V-5 M0 5 V11 M-11 0 H-5 M5 0 H11"/></g></symbol>
      <symbol id="ic-team" viewBox="-12 -12 24 24"><g fill="#fff"><circle cx="-6.5" cy="-5" r="2.6"/><circle cx="0" cy="-6" r="2.8"/><circle cx="6.5" cy="-5" r="2.6"/><rect x="-9.5" y="-1.5" width="6" height="10" rx="2"/><rect x="-3" y="-2.5" width="6" height="11" rx="2"/><rect x="3.5" y="-1.5" width="6" height="10" rx="2"/></g></symbol>
      <symbol id="ic-growth" viewBox="-12 -12 24 24"><g fill="none" stroke="#fff" stroke-width="2" stroke-linejoin="round" stroke-linecap="round"><polyline points="-10,7 -4,1 0,4 8,-5"/><polyline points="3,-6 8,-5 7,0"/><path d="M-10 10 H10"/></g></symbol>
      <symbol id="ic-gear" viewBox="-12 -12 24 24"><g fill="none" stroke="#fff" stroke-width="2"><circle r="7" stroke-dasharray="3 2.5" stroke-width="3.5"/><circle r="3"/></g></symbol>
      <symbol id="ic-star" viewBox="-12 -12 24 24"><polygon fill="#fff" points="0,-10 2.6,-3.3 9.5,-3.1 4.1,1.3 5.9,8.1 0,4.2 -5.9,8.1 -4.1,1.3 -9.5,-3.1 -2.6,-3.3"/></symbol>
      <symbol id="ic-trophy" viewBox="-12 -12 24 24"><g fill="none" stroke="#fff" stroke-width="2" stroke-linejoin="round" stroke-linecap="round"><path d="M-6 -9 H6 V-2 A6 6 0 0 1 -6 -2 Z"/><path d="M-6 -7 H-9 A3.5 3.5 0 0 0 -5.5 0 M6 -7 H9 A3.5 3.5 0 0 1 5.5 0"/><path d="M0 4 V7 M-5 10 H5 M-3 7 H3 V10 H-3 Z"/></g></symbol>
      <symbol id="ic-search" viewBox="-12 -12 24 24"><g fill="none" stroke="#fff" stroke-width="2.2" stroke-linecap="round"><circle cx="-2" cy="-2" r="6.5"/><path d="M3 3 L9 9"/><polyline points="-6,-2 -4,-2 -3,-4.5 -1,0.5 0,-2 2,-2" stroke-width="1.6"/></g></symbol>
    </defs>
  </svg>

  <p class="sheet-label sheet-label--one">Sample One</p>

  <!-- ===== Board one: outline version ===== -->
  <svg class="board board--one diagram--outline" viewBox="0 0 1595 898" width="936" height="527">
    <rect class="panel-bg" width="1595" height="898"/>
    <ellipse class="map-area" cx="820" cy="420" rx="720" ry="420" role="img" aria-label="Faint dotted world map in the background"/>

    <!-- foundation semicircle -->
    <g class="foundation">
      <path class="wedge wedge-01" d="M715 438 L382 438 A333 333 0 0 1 445.6 242.2 Z"/>
      <path class="wedge wedge-02" d="M715 438 L445.6 242.2 A333 333 0 0 1 612.1 121.3 Z"/>
      <path class="wedge wedge-03" d="M715 438 L612.1 121.3 A333 333 0 0 1 817.9 121.3 Z"/>
      <path class="wedge wedge-04" d="M715 438 L817.9 121.3 A333 333 0 0 1 984.4 242.2 Z"/>
      <path class="wedge wedge-05" d="M715 438 L984.4 242.2 A333 333 0 0 1 1048 438 Z"/>
      <path class="hub-ring" d="M575 438 A140 140 0 0 1 855 438 Z"/>
      <path class="divider" d="M715 438 L440 238.1 M715 438 L609.9 114.6 M715 438 L820.1 114.6 M715 438 L990 238.1"/>
      <path class="hub" d="M617 438 A98 98 0 0 1 813 438 Z"/>
      <text class="hub-title" x="715"><tspan x="715" y="392">Capabilities</tspan><tspan x="715" y="415">driving a solid</tspan><tspan x="715" y="437">foundation</tspan></text>
      <text class="step-no" x="598" y="410">01</text>
      <text class="step-no" x="642" y="348">02</text>
      <text class="step-no" x="713" y="325">03</text>
      <text class="step-no" x="785" y="348">04</text>
      <text class="step-no" x="828" y="410">05</text>
      <text class="step-label"><tspan x="486" y="362">Discover your</tspan><tspan x="486" y="383">purpose. Why</tspan><tspan x="486" y="404">Do you exist?</tspan></text>
      <text class="step-label"><tspan x="565" y="220">Identify</tspan><tspan x="565" y="241">Purpose</tspan><tspan x="565" y="262">Activators</tspan><tspan x="565" y="283">(Vision)</tspan></text>
      <text class="step-label"><tspan x="713" y="181">Develop a</tspan><tspan x="713" y="202">Master plan</tspan><tspan x="713" y="223">(strategy)</tspan></text>
      <text class="step-label"><tspan x="860" y="220">Cultivate</tspan><tspan x="860" y="241">Psychological</tspan><tspan x="860" y="262">Safety and</tspan><tspan x="860" y="283">Ownership</tspan></text>
      <text class="step-label"><tspan x="941" y="362">Tap into peoples</tspan><tspan x="941" y="383">Purpose and Passion</tspan><tspan x="941" y="404">(intrinsic motivation)</tspan></text>
      <text class="restart" x="476" y="466">(Re)Start Here  |  (Re)Invent Here</text>
    </g>

    <!-- excellence semicircle -->
    <g class="excellence">
      <path class="wedge wedge-06" d="M1150 458 L817 458 A333 333 0 0 0 880.6 653.8 Z"/>
      <path class="wedge wedge-07" d="M1150 458 L880.6 653.8 A333 333 0 0 0 1047.1 774.7 Z"/>
      <path class="wedge wedge-08" d="M1150 458 L1047.1 774.7 A333 333 0 0 0 1252.9 774.7 Z"/>
      <path class="wedge wedge-09" d="M1150 458 L1252.9 774.7 A333 333 0 0 0 1419.4 653.8 Z"/>
      <path class="wedge wedge-10" d="M1150 458 L1419.4 653.8 A333 333 0 0 0 1483 458 Z"/>
      <path class="hub-ring" d="M1010 458 A140 140 0 0 0 1290 458 Z"/>
      <path class="divider" d="M1150 458 L875 657.9 M1150 458 L1044.9 781.4 M1150 458 L1255.1 781.4 M1150 458 L1425 657.9"/>
      <path class="hub" d="M1052 458 A98 98 0 0 0 1248 458 Z"/>
      <text class="hub-title"><tspan x="1152" y="473">Capabilities</tspan><tspan x="1152" y="496">maximizing</tspan><tspan x="1152" y="519">excellence</tspan></text>
      <text class="step-no" x="1037" y="482">06</text>
      <text class="step-no" x="1082" y="545">07</text>
      <text class="step-no" x="1152" y="568">08</text>
      <text class="step-no" x="1223" y="545">09</text>
      <text class="step-no" x="1268" y="482">10</text>
      <text class="step-label"><tspan x="921" y="498">Unlock culture of</tspan><tspan x="921" y="519">personal growth</tspan><tspan x="921" y="540">&amp; development</tspan></text>
      <text class="step-label"><tspan x="1002" y="632">Prioritize</tspan><tspan x="1002" y="653">Feedback &amp;</tspan><tspan x="1002" y="674">Transparency</tspan></text>
      <text class="step-label"><tspan x="1155" y="687">Empower the</tspan><tspan x="1155" y="708">community from</tspan><tspan x="1155" y="729">bottom-up</tspan></text>
      <text class="step-label"><tspan x="1308" y="632">Put excellent</tspan><tspan x="1308" y="653">(team) performance</tspan><tspan x="1308" y="674">in the spotlight</tspan></text>
      <text class="step-label"><tspan x="1377" y="498">Monitor</tspan><tspan x="1377" y="519">engagement</tspan><tspan x="1377" y="540">Real-time</tspan></text>
    </g>

    <!-- rings -->
    <path class="ring" d="M295 438 A420 420 0 0 1 1135 438"/>
    <path class="ring" d="M732 458 A418 418 0 0 0 1568 458"/>
    <path id="arcTopA" d="M303 438 A412 412 0 0 1 1127 438" fill="none"/>
    <path id="arcBottomA" d="M724 458 A426 426 0 0 0 1576 458" fill="none"/>
    <text class="ring-text"><textPath href="#arcTopA" startOffset="17%">SELF DIRECTION</textPath></text>
    <text class="ring-text"><textPath href="#arcTopA" startOffset="67.5%">HUMAN EXPERIENCE</textPath></text>
    <text class="ring-text" letter-spacing="7"><textPath href="#arcBottomA" startOffset="45%">UNLEASH ENGAGEMENT</textPath></text>
    <polygon class="ring-arrow" transform="translate(607 63) rotate(-16)" points="-10,-8 11,0 -10,8 -5,0"/>
    <polygon class="ring-arrow" transform="translate(1117 395) rotate(84)" points="-10,-8 11,0 -10,8 -5,0"/>
    <polygon class="ring-arrow" transform="translate(1452 703) rotate(-51)" points="-10,-8 11,0 -10,8 -5,0"/>

    <!-- step markers -->
    <g transform="translate(399 335)"><circle class="marker-disc m01" r="28"/><use href="#ic-pulse" x="-13" y="-13" width="26" height="26"/></g>
    <g transform="translate(520 169)"><circle class="marker-disc m02" r="28"/><use href="#ic-scope" x="-13" y="-13" width="26" height="26"/></g>
    <g transform="translate(715 106)"><circle class="marker-disc m03" r="28"/><use href="#ic-target" x="-13" y="-13" width="26" height="26"/></g>
    <g transform="translate(910 169)"><circle class="marker-disc m04" r="28"/><use href="#ic-team" x="-13" y="-13" width="26" height="26"/></g>
    <g transform="translate(1031 335)"><circle class="marker-disc m05" r="28"/><use href="#ic-pulse" x="-13" y="-13" width="26" height="26"/></g>
    <g transform="translate(834 561)"><circle class="marker-disc m06" r="28"/><use href="#ic-growth" x="-13" y="-13" width="26" height="26"/></g>
    <g transform="translate(955 727)"><circle class="marker-disc m07" r="28"/><use href="#ic-gear" x="-13" y="-13" width="26" height="26"/></g>
    <g transform="translate(1150 790)"><circle class="marker-disc m08" r="28"/><use href="#ic-star" x="-13" y="-13" width="26" height="26"/></g>
    <g transform="translate(1345 727)"><circle class="marker-disc m09" r="28"/><use href="#ic-trophy" x="-13" y="-13" width="26" height="26"/></g>
    <g transform="translate(1466 561)"><circle class="marker-disc m10" r="28"/><use href="#ic-search" x="-13" y="-13" width="26" height="26"/></g>

    <!-- title -->
    <text class="title" x="70" y="618" textLength="620" lengthAdjust="spacingAndGlyphs">THE <tspan class="title-accent">KEYSTRIDE</tspan></text>
    <text class="title" x="70" y="703" textLength="518" lengthAdjust="spacingAndGlyphs">PRINCIPLES</text>
    <text class="subtitle"><tspan x="72" y="762">Liberate The Workplace Unleashing Value</tspan><tspan x="72" y="794">Throug Purpose At Every Level Of Scale</tspan></text>

    <!-- goal -->
    <path class="goal-box" d="M1370 88 L1518 175 L1485 175 L1485 438 L1256 438 L1256 175 L1223 175 Z"/>
    <g class="goal-gem" transform="translate(1370 143)"><path d="M-24 -6 L-14 -18 H14 L24 -6 L0 20 Z M-24 -6 H24 M-14 -18 L-7 -6 L0 20 L7 -6 L14 -18 M-7 -6 L0 -18 L7 -6"/></g>
    <text class="goal-title"><tspan x="1370" y="216">REACHING FULL</tspan><tspan x="1370" y="239">POTENTIAL OF PEOPLE</tspan><tspan x="1370" y="262">AND ORGANIZATION</tspan></text>
    <text class="goal-list"><tspan x="1284" y="293">• Productivity up to 800%</tspan><tspan x="1284" y="315">• Employee engagement &gt;90%</tspan><tspan x="1284" y="336">• Max discretionary effort gap</tspan><tspan x="1284" y="358">• High resilience to change</tspan></text>
  </svg>

  <!-- ===== Board two: solid colour version ===== -->
  <svg class="board board--two diagram--solid" viewBox="0 0 1595 898" width="936" height="527">
    <rect class="panel-bg" width="1595" height="898"/>
    <ellipse class="map-area" cx="820" cy="420" rx="720" ry="420" role="img" aria-label="Faint dotted world map in the background"/>

    <g class="foundation">
      <path class="wedge wedge-01" d="M715 438 L382 438 A333 333 0 0 1 445.6 242.2 Z"/>
      <path class="wedge wedge-02" d="M715 438 L445.6 242.2 A333 333 0 0 1 612.1 121.3 Z"/>
      <path class="wedge wedge-03" d="M715 438 L612.1 121.3 A333 333 0 0 1 817.9 121.3 Z"/>
      <path class="wedge wedge-04" d="M715 438 L817.9 121.3 A333 333 0 0 1 984.4 242.2 Z"/>
      <path class="wedge wedge-05" d="M715 438 L984.4 242.2 A333 333 0 0 1 1048 438 Z"/>
      <path class="hub-ring" d="M575 438 A140 140 0 0 1 855 438 Z"/>
      <path class="divider" d="M715 438 L440 238.1 M715 438 L609.9 114.6 M715 438 L820.1 114.6 M715 438 L990 238.1"/>
      <path class="hub" d="M617 438 A98 98 0 0 1 813 438 Z"/>
      <text class="hub-title"><tspan x="715" y="392">Capabilities</tspan><tspan x="715" y="415">driving a solid</tspan><tspan x="715" y="437">foundation</tspan></text>
      <text class="step-no" x="598" y="410">01</text>
      <text class="step-no" x="642" y="348">02</text>
      <text class="step-no" x="713" y="325">03</text>
      <text class="step-no" x="785" y="348">04</text>
      <text class="step-no" x="828" y="410">05</text>
      <text class="step-label"><tspan x="486" y="362">Discover your</tspan><tspan x="486" y="383">purpose. Why</tspan><tspan x="486" y="404">Do you exist?</tspan></text>
      <text class="step-label"><tspan x="565" y="220">Identify</tspan><tspan x="565" y="241">Purpose</tspan><tspan x="565" y="262">Activators</tspan><tspan x="565" y="283">(Vision)</tspan></text>
      <text class="step-label"><tspan x="713" y="181">Develop a</tspan><tspan x="713" y="202">Master plan</tspan><tspan x="713" y="223">(strategy)</tspan></text>
      <text class="step-label"><tspan x="860" y="220">Cultivate</tspan><tspan x="860" y="241">Psychological</tspan><tspan x="860" y="262">Safety and</tspan><tspan x="860" y="283">Ownership</tspan></text>
      <text class="step-label"><tspan x="941" y="362">Tap into peoples</tspan><tspan x="941" y="383">Purpose and Passion</tspan><tspan x="941" y="404">(intrinsic motivation)</tspan></text>
      <text class="restart" x="476" y="466">(Re)Start Here  |  (Re)Invent Here</text>
    </g>

    <g class="excellence">
      <path class="wedge wedge-06" d="M1150 458 L817 458 A333 333 0 0 0 880.6 653.8 Z"/>
      <path class="wedge wedge-07" d="M1150 458 L880.6 653.8 A333 333 0 0 0 1047.1 774.7 Z"/>
      <path class="wedge wedge-08" d="M1150 458 L1047.1 774.7 A333 333 0 0 0 1252.9 774.7 Z"/>
      <path class="wedge wedge-09" d="M1150 458 L1252.9 774.7 A333 333 0 0 0 1419.4 653.8 Z"/>
      <path class="wedge wedge-10" d="M1150 458 L1419.4 653.8 A333 333 0 0 0 1483 458 Z"/>
      <path class="hub-ring" d="M1010 458 A140 140 0 0 0 1290 458 Z"/>
      <path class="divider" d="M1150 458 L875 657.9 M1150 458 L1044.9 781.4 M1150 458 L1255.1 781.4 M1150 458 L1425 657.9"/>
      <path class="hub" d="M1052 458 A98 98 0 0 0 1248 458 Z"/>
      <text class="hub-title"><tspan x="1152" y="473">Capabilities</tspan><tspan x="1152" y="496">maximizing</tspan><tspan x="1152" y="519">excellence</tspan></text>
      <text class="step-no" x="1037" y="482">06</text>
      <text class="step-no" x="1082" y="545">07</text>
      <text class="step-no" x="1152" y="568">08</text>
      <text class="step-no" x="1223" y="545">09</text>
      <text class="step-no" x="1268" y="482">10</text>
      <text class="step-label"><tspan x="921" y="498">Unlock culture of</tspan><tspan x="921" y="519">personal growth</tspan><tspan x="921" y="540">&amp; development</tspan></text>
      <text class="step-label"><tspan x="1002" y="632">Prioritize</tspan><tspan x="1002" y="653">Feedback &amp;</tspan><tspan x="1002" y="674">Transparency</tspan></text>
      <text class="step-label"><tspan x="1155" y="687">Empower the</tspan><tspan x="1155" y="708">community from</tspan><tspan x="1155" y="729">bottom-up</tspan></text>
      <text class="step-label"><tspan x="1308" y="632">Put excellent</tspan><tspan x="1308" y="653">(team) performance</tspan><tspan x="1308" y="674">in the spotlight</tspan></text>
      <text class="step-label"><tspan x="1377" y="498">Monitor</tspan><tspan x="1377" y="519">engagement</tspan><tspan x="1377" y="540">Real-time</tspan></text>
    </g>

    <path class="ring" d="M295 438 A420 420 0 0 1 1135 438"/>
    <path class="ring" d="M732 458 A418 418 0 0 0 1568 458"/>
    <path id="arcTopB" d="M303 438 A412 412 0 0 1 1127 438" fill="none"/>
    <path id="arcBottomB" d="M724 458 A426 426 0 0 0 1576 458" fill="none"/>
    <text class="ring-text"><textPath href="#arcTopB" startOffset="17%">SELF DIRECTION</textPath></text>
    <text class="ring-text"><textPath href="#arcTopB" startOffset="67.5%">HUMAN EXPERIENCE</textPath></text>
    <text class="ring-text" letter-spacing="7"><textPath href="#arcBottomB" startOffset="45%">UNLEASH ENGAGEMENT</textPath></text>
    <polygon class="ring-arrow" transform="translate(607 63) rotate(-16)" points="-10,-8 11,0 -10,8 -5,0"/>
    <polygon class="ring-arrow" transform="translate(1117 395) rotate(84)" points="-10,-8 11,0 -10,8 -5,0"/>
    <polygon class="ring-arrow" transform="translate(1452 703) rotate(-51)" points="-10,-8 11,0 -10,8 -5,0"/>

    <g transform="translate(399 335)"><circle class="marker-disc m01" r="28"/><use href="#ic-pulse" x="-13" y="-13" width="26" height="26"/></g>
    <g transform="translate(520 169)"><circle class="marker-disc m02" r="28"/><use href="#ic-scope" x="-13" y="-13" width="26" height="26"/></g>
    <g transform="translate(715 106)"><circle class="marker-disc m03" r="28"/><use href="#ic-target" x="-13" y="-13" width="26" height="26"/></g>
    <g transform="translate(910 169)"><circle class="marker-disc m04" r="28"/><use href="#ic-team" x="-13" y="-13" width="26" height="26"/></g>
    <g transform="translate(1031 335)"><circle class="marker-disc m05" r="28"/><use href="#ic-pulse" x="-13" y="-13" width="26" height="26"/></g>
    <g transform="translate(834 561)"><circle class="marker-disc m06" r="28"/><use href="#ic-growth" x="-13" y="-13" width="26" height="26"/></g>
    <g transform="translate(955 727)"><circle class="marker-disc m07" r="28"/><use href="#ic-gear" x="-13" y="-13" width="26" height="26"/></g>
    <g transform="translate(1150 790)"><circle class="marker-disc m08" r="28"/><use href="#ic-star" x="-13" y="-13" width="26" height="26"/></g>
    <g transform="translate(1345 727)"><circle class="marker-disc m09" r="28"/><use href="#ic-trophy" x="-13" y="-13" width="26" height="26"/></g>
    <g transform="translate(1466 561)"><circle class="marker-disc m10" r="28"/><use href="#ic-search" x="-13" y="-13" width="26" height="26"/></g>

    <text class="title" x="70" y="618" textLength="620" lengthAdjust="spacingAndGlyphs">THE <tspan class="title-accent">KEYSTRIDE</tspan></text>
    <text class="title" x="70" y="703" textLength="518" lengthAdjust="spacingAndGlyphs">PRINCIPLES</text>
    <text class="subtitle"><tspan x="72" y="762">Liberate The Workplace Unleashing Value</tspan><tspan x="72" y="794">Throug Purpose At Every Level Of Scale</tspan></text>

    <path class="goal-box" d="M1370 88 L1518 175 L1485 175 L1485 438 L1256 438 L1256 175 L1223 175 Z"/>
    <g class="goal-gem" transform="translate(1370 143)"><path d="M-24 -6 L-14 -18 H14 L24 -6 L0 20 Z M-24 -6 H24 M-14 -18 L-7 -6 L0 20 L7 -6 L14 -18 M-7 -6 L0 -18 L7 -6"/></g>
    <text class="goal-title"><tspan x="1370" y="216">REACHING FULL</tspan><tspan x="1370" y="239">POTENTIAL OF PEOPLE</tspan><tspan x="1370" y="262">AND ORGANIZATION</tspan></text>
    <text class="goal-list"><tspan x="1284" y="293">• Productivity up to 800%</tspan><tspan x="1284" y="315">• Employee engagement &gt;90%</tspan><tspan x="1284" y="336">• Max discretionary effort gap</tspan><tspan x="1284" y="358">• High resilience to change</tspan></text>
  </svg>

  <p class="sheet-label sheet-label--two">Sample Two</p>
</div>
</body>
</html>
```